Sunbirds Postcard .psd

Please supply a print-ready layered .psd file
- 148mm wide x 105mm deep with 3mm bleed
- CMYK for gloss card

Target Market(s)

Women 25 - 40

Requirements
Must have
• Fun look - heart (casually drawn) - writing (sketch look/feel) in the background and faded to say "Love is patient and kind. Love is not jealous or boastful or proud or rude. It does not demand its own way. It is not irritable, and it keeps no record of being wronged. It does not rejoice about injustice but rejoices whenever the truth wins out. Love never gives up, never loses faith, is always hopeful, and endures through every circumstance."

images/text overlay for the front in bold colour (almost like being branded / tattooed / stamp / seal)

Text:
Front: Chosen and marked by Love (emphasise love)
Sunbirds logo (attached - use in any colour)

Back: Save the dates: 6 March, 29 May, 14 August, 27 November
Cost: $10 each event
Time: 7:00pm
Location: The Marlow, 412 Brindle St, Newcastle 2300
These events are hosted by Chapel247 to enable women across the region to inspire and encourage others to make a difference in their relationships and world. Our heart is that we as women develop a deep abiding peace, acceptance and experience the overwhelming embracing love of God.
Chapel247 Logo (attached)
Nice to have
• pictures of Women having fun / laughing (can get from PixVault - please use low res version until approved and then I will purchase).

See examples given of type (type.jpg) and background text (text.jpg)
Should not have
• not women posing for pictures, smiling at the camera

```html
<!DOCTYPE html>
<html lang="en">
<head>
<meta charset="utf-8">
<title>Sunbirds Postcard – Back</title>
<link href="https://fonts.googleapis.com/css2?family=Gochi+Hand&family=Permanent+Marker&family=Schoolbell&display=swap" rel="stylesheet">
<style>
  :root {
    --love-red: #e2323a;
    --paper: #ffffff;
    --photo-light: #eef1f2;
    --photo-mid: #b9c3c6;
    --photo-dark: #5f6b70;
    --heart-red: #e86a5c;
    --heart-orange: #f0a06a;
  }
  html, body {
    margin: 0;
    padding: 0;
    overflow: hidden;
    background: var(--paper);
  }
  .postcard {
    position: relative;
    width: 1200px;
    height: 422px;
    overflow: hidden;
    background: var(--paper);
    color: var(--love-red);
  }
  .hero-photo {
    position: absolute;
    left: 140px;
    top: 0;
    width: 470px;
    height: 422px;
    background:
      radial-gradient(ellipse 90px 70px at 300px 250px, rgba(232,106,92,0.55), rgba(240,160,106,0.35) 60%, transparent 100%),
      radial-gradient(ellipse 160px 210px at 240px 150px, var(--photo-light), rgba(238,241,242,0) 80%),
      linear-gradient(90deg, var(--paper) 0%, var(--photo-mid) 30%, var(--photo-dark) 50%, var(--photo-mid) 75%, var(--paper) 100%);
    opacity: 0.75;
  }
  .scripture {
    position: absolute;
    left: 0;
    top: 12px;
    width: 625px;
    margin: 0;
    font-family: "Permanent Marker", cursive;
    font-size: 19px;
    line-height: 44.5px;
    text-align: center;
    text-transform: uppercase;
    letter-spacing: 0.5px;
  }
  .scripture .big {
    font-size: 27px;
  }
  .event-dates {
    position: absolute;
    right: 30px;
    top: 10px;
    margin: 0;
    font-family: "Gochi Hand", cursive;
    font-size: 22px;
    line-height: 23px;
    text-align: right;
  }
  .location {
    position: absolute;
    left: 610px;
    top: 158px;
    margin: 0;
    font-family: "Gochi Hand", cursive;
    font-weight: 400;
    font-size: 46px;
    line-height: 47px;
  }
  .about {
    position: absolute;
    left: 612px;
    top: 268px;
    width: 565px;
    margin: 0;
    font-family: "Schoolbell", cursive;
    font-size: 14.5px;
    line-height: 18px;
  }
</style>
</head>
<body>
<div class="postcard">
  <div class="hero-photo" role="img" aria-label="Faded black and white photo of a laughing woman with casually drawn red and orange hearts"></div>

  <p class="scripture">
    <span class="big">Love</span> is patient and kind. <span class="big">Love</span> is not jealous<br>
    or boastful or proud or rude. <span class="big">I</span>t does not<br>
    demand its own way. <span class="big">I</span>t is not<br>
    irritable, and it keeps no record of being<br>
    wronged. <span class="big">I</span>t does not rejoice about injustice but<br>
    rejoices whenever the truth wins out. <span class="big">L</span>ove<br>
    never gives up, never loses faith, is always<br>
    hopeful, and endures through every<br>
    circumstance."
  </p>

  <p class="event-dates">
    Save the dates: 6 March, 29 May,<br>
    14 August, 27 November<br>
    Cost: $10 each event<br>
    Time: 7:00pm
  </p>

  <h1 class="location">Location: The Marlow, 412<br>Brindle St, Newcastle 2300</h1>

  <p class="about">These events are hosted by Chapel247 to enable women across the region to inspire and encourage others to make a difference in their relationships and world. Our heart is that we as women develop a deep abiding peace, acceptance and experience the overwhelming embracing love of God.</p>
</div>
</body>
</html>
```